Lumora Learning Web Design Project

Who We are:
Lumora Learning is education information portal/ magazine, providing information about the Chinese and International education markets. Our aim is to help school principals improve there curriculum, and parents in understanding this curriculum.

Project Brief:
The site will include education news updates, educational services, curriculum developments and overseas study. We hope the site represents the cross cultural bridge between the west and east. The site will cover both the Sciences and Arts.

Note:
The logo design competition is also underway so we only need the website design

What We want:
This competition is for Design only no coding!
Design a home page based on Template 1,2 or 3. I only need to select one.
The design of an article page.

Optional
Design a Microsoft Windows metro style splash page.

Sites We like:
http://www.kavelin.com.cn/kavelinlingo/default.aspx
http://www.brixtalacademia.co.uk/
http://qrpv.norvatestudio.net/

Template Explanations:
Template 1-
The main information has a dynamic sliding category view that when clicked displays the relevant info.
In addition to the main upper menu it also has a left hand sliding menu that pops out on click or gesture

Template 2-
Has limited number of Articles most of the menus are drop downs from the top menu

Template 3-
No Top menu

Target Market(s)

Teachers, principals and parents

Industry/Entity Type

Education

Requirements
Should not have
• kindergarten preschool feel

```html
<!DOCTYPE html>
<html lang="en">
<head>
<meta charset="utf-8">
<title>Lumora Learning</title>
<link href="https://fonts.googleapis.com/css2?family=Roboto:ital,wght@0,300;0,400;0,500;1,300&display=swap" rel="stylesheet">
<style>
:root{
  --bg-core:#d8563f;
  --bg-mid:#9a2c4a;
  --bg-edge:#3a1745;
  --bg-deep:#22143a;
  --white:#ffffff;
  --soft-white:rgba(255,255,255,.78);
  --faint-white:rgba(255,255,255,.5);
  --glass:rgba(255,255,255,.2);
  --glass-strong:rgba(255,255,255,.26);
  --title:#b2325d;
  --button:#7b1f3f;
  --body-text:#8a8a8a;
  --date-bg:#e6e6e6;
  --footer:#1f1620;
}
*{margin:0;padding:0;box-sizing:border-box}
html,body{width:1200px;height:875px;overflow:hidden}
body{
  position:relative;
  font-family:'Roboto',sans-serif;
  font-weight:300;
  color:var(--white);
  background:
    radial-gradient(ellipse 520px 380px at 600px 450px,#e8764a 0%,rgba(216,86,63,.6) 45%,rgba(216,86,63,0) 100%),
    radial-gradient(ellipse 900px 600px at 600px 430px,var(--bg-core) 0%,var(--bg-mid) 55%,var(--bg-edge) 85%,var(--bg-deep) 100%);
}
.abs{position:absolute}
.brand{left:305px;top:26px;font-size:23px;font-weight:300;letter-spacing:.2px}
.header-divider{left:528px;top:18px;width:1px;height:38px;background:var(--faint-white)}
.tagline{left:561px;top:33px;font-size:15px;font-style:italic;color:var(--faint-white)}

.slide-arrow{top:176px;width:44px;height:43px;background:rgba(255,255,255,.18);border-radius:2px;display:flex;align-items:center;justify-content:center}
.slide-arrow.prev{left:31px}.slide-arrow.next{left:1124px}

.main-nav{left:269px;top:73px;width:662px;height:37px;background:rgba(200,140,170,.45);border-radius:3px 3px 0 0;font-size:11px}
.nav-home{position:absolute;left:30px;top:4px;width:28px;height:28px;background:rgba(255,255,255,.18);border-radius:2px;display:flex;align-items:center;justify-content:center}
.nav-item{position:absolute;top:12px;color:var(--white);font-weight:400}
.nav-item.active{top:5px;left:431px;width:78px;height:27px;background:var(--white);color:#666;border-radius:2px;padding:7px 0 0 14px}

.hero{left:269px;top:110px;width:662px;height:212px;background:linear-gradient(90deg,#b74a3e 0%,#d6d6cf 22%,#d9d9d3 38%,#5f8a3f 52%,#4e7d36 75%,#5e8c45 100%);box-shadow:0 3px 8px rgba(0,0,0,.3)}
.dropdown{left:700px;top:115px;width:122px;height:96px;background:var(--white);border-radius:2px;box-shadow:0 2px 6px rgba(0,0,0,.2);font-size:9px;color:#444;font-weight:400}
.dropdown li{list-style:none;position:absolute;left:13px}
.dropdown .current{left:10px;font-weight:500;color:#222}

.slider-dots{left:578px;top:338px;display:flex;gap:6px}
.slider-dots span{width:6px;height:6px;border:1px solid var(--soft-white);border-radius:50%}
.slider-dots span.on{background:var(--white)}

.post{top:367px;width:212px;height:199px;background:var(--white);border-radius:3px;box-shadow:0 2px 6px rgba(0,0,0,.2)}
.post h2{position:absolute;left:19px;top:16px;width:180px;font-size:16px;font-weight:300;color:var(--title);line-height:19px}
.post-date{position:absolute;left:19px;width:112px;height:18px;background:var(--date-bg);font-size:8.5px;color:#666;font-weight:400;padding:4px 0 0 10px}
.post p{position:absolute;left:19px;width:176px;font-size:8px;line-height:11.3px;color:var(--body-text);font-weight:400}
.post-button{position:absolute;left:19px;top:168px;width:62px;height:18px;background:var(--button);font-size:8.5px;color:var(--white);font-weight:400;padding:4px 0 0 7px}
.post-image{position:absolute;left:0;top:40px;width:212px;height:62px;background:linear-gradient(90deg,#d9d9d9,#777 40%,#b8b8b8 70%,#444)}

.banner{left:763px;top:367px;width:143px;height:255px;background:linear-gradient(180deg,rgba(255,255,255,.28),rgba(255,255,255,.14));border:1px solid rgba(255,255,255,.35);border-radius:3px;display:flex;align-items:center;justify-content:center;text-align:center;font-size:14.5px;line-height:15px;color:var(--soft-white)}

.utility-bar{left:294px;top:580px;width:443px;height:42px;background:rgba(255,255,255,.26);border-radius:3px}
.social-label{position:absolute;left:19px;top:13px;font-size:13px;color:var(--soft-white)}
.social-dot{position:absolute;top:16px;width:10px;height:10px;border-radius:50%;background:var(--white)}
.utility-divider{position:absolute;left:248px;top:0;width:1px;height:42px;background:rgba(120,40,60,.35)}
.search-field{position:absolute;left:268px;top:16px;font-size:8.5px;color:var(--soft-white);font-weight:400}
.search-icon{position:absolute;left:410px;top:13px}

.section-title{top:659px;font-size:19px;font-weight:300}
.section-rule{top:692px;height:1px;background:rgba(255,255,255,.3)}
.quick-menu a{position:absolute;font-size:8.5px;color:var(--soft-white);text-decoration:none;font-weight:400}
.quick-menu a.current{color:var(--white);font-weight:500}
.contact-field{left:763px;width:143px;background:rgba(255,255,255,.22);font-size:8.5px;font-weight:400;padding:8px 0 0 9px}
.send-button{left:877px;top:795px;width:25px;height:19px;background:var(--white);display:flex;align-items:center;justify-content:center}

.site-footer{left:0;top:837px;width:1200px;height:38px;background:var(--footer);text-align:center;font-size:7.5px;color:#9a8f95;font-weight:400;padding-top:14px}
.site-footer strong{color:#d9d0d5;font-weight:400}
</style>
</head>
<body>
<header>
  <div class="abs brand">LumoraLearning.com</div>
  <div class="abs header-divider"></div>
  <div class="abs tagline">Improve &amp; understand your curriculum..</div>
</header>

<div class="abs slide-arrow prev"><svg width="14" height="22" viewBox="0 0 14 22"><path d="M12 2 L3 11 L12 20" fill="none" stroke="#fff" stroke-opacity=".7" stroke-width="2.5"/></svg></div>
<div class="abs slide-arrow next"><svg width="14" height="22" viewBox="0 0 14 22"><path d="M2 2 L11 11 L2 20" fill="none" stroke="#fff" stroke-opacity=".7" stroke-width="2.5"/></svg></div>

<nav class="abs main-nav">
  <div class="nav-home"><svg width="13" height="12" viewBox="0 0 13 12"><path d="M1 6 L6.5 1 L12 6 M3 5 V11 H10 V5" fill="none" stroke="#fff" stroke-width="1"/></svg></div>
  <span class="nav-item" style="left:75px">About us</span>
  <span class="nav-item" style="left:138px">Portfolio</span>
  <span class="nav-item" style="left:199px">What is curriculum?</span>
  <span class="nav-item" style="left:312px">What can we do for you?</span>
  <span class="nav-item active">Services <svg width="7" height="5" viewBox="0 0 7 5" style="margin-left:6px"><path d="M1 1 L3.5 3.5 L6 1" fill="none" stroke="#666" stroke-width="1.2"/></svg></span>
  <span class="nav-item" style="left:519px">Contact us</span>
</nav>

<div class="abs hero" role="img" aria-label="Hand holding a red and white megaphone in front of a green chalkboard covered with the word JOB"></div>

<ul class="abs dropdown">
  <li style="top:15px">Curriculum writing</li>
  <li class="current" style="top:34px">› &nbsp;Curriculum editation</li>
  <li style="top:53px">Copywriting</li>
  <li style="top:72px">Guidance</li>
</ul>

<div class="abs slider-dots"><span></span><span class="on"></span><span></span><span></span></div>

<article class="abs post" style="left:294px">
  <h2>Aliquam id mauris vel mi blandit pellentesque</h2>
  <div class="post-date" style="top:59px">1 july 2013 @ 10:59 AM</div>
  <p style="top:91px">Morbi euismod libero sit amet mattis laoreet. Nulla rutrum leo arcu. Phasellus sodales egestas neque at facilisis. Fusce semper arcu sit amet eros elementum, vel consequat dolor sodales. In eu massa eu elit condimentum pulvinar eu vel elit..</p>
  <div class="post-button">More details</div>
</article>

<article class="abs post" style="left:525px">
  <h2>Duis tempus augue vitae</h2>
  <div class="post-image" role="img" aria-label="Black and white close-up of a typewriter with a sheet reading curriculum vitae"></div>
  <div class="post-date" style="top:109px">1 july 2013 @ 10:59 AM</div>
  <p style="top:134px">Phasellus aliquet elit arcu. Sed ornare orci eget lorem euismod, ac vulputate mi..</p>
  <div class="post-button">More details</div>
</article>

<aside class="abs banner">Banner<br>advertisement</aside>

<div class="abs utility-bar">
  <span class="social-label">Social Media:</span>
  <span class="social-dot" style="left:109px" aria-label="Social network one"></span>
  <span class="social-dot" style="left:142px" aria-label="Social network two"></span>
  <span class="social-dot" style="left:177px" aria-label="Social network three"></span>
  <span class="social-dot" style="left:213px" aria-label="Social network four"></span>
  <div class="utility-divider"></div>
  <span class="search-field">Search term here..</span>
  <svg class="search-icon" width="15" height="15" viewBox="0 0 15 15"><circle cx="6" cy="6" r="4.5" fill="none" stroke="#fff" stroke-width="1.8"/><path d="M9.5 9.5 L13.5 13.5" stroke="#fff" stroke-width="2"/></svg>
</div>

<h3 class="abs section-title" style="left:312px">Quick Menu</h3>
<div class="abs section-rule" style="left:294px;width:443px"></div>
<nav class="quick-menu">
  <a class="abs" style="left:312px;top:707px">Morbi euismod</a>
  <a class="abs" style="left:312px;top:730px">Libero sit</a>
  <a class="abs current" style="left:302px;top:752px">› &nbsp;Amet mattis laoreet</a>
  <a class="abs" style="left:312px;top:775px">Nulla rutrum</a>
  <a class="abs" style="left:312px;top:797px">Leo arc</a>
  <a class="abs" style="left:443px;top:707px">Phasellus aliquet elit</a>
  <a class="abs" style="left:443px;top:730px">Arcu sed</a>
  <a class="abs" style="left:443px;top:752px">Ornare orci eget</a>
  <a class="abs" style="left:443px;top:775px">Lorem euismod, ac</a>
  <a class="abs" style="left:443px;top:797px">Vulputate mi fermentum</a>
  <a class="abs" style="left:593px;top:707px">Quisque tortor</a>
  <a class="abs" style="left:593px;top:730px">Nisl lacinia vitae</a>
  <a class="abs" style="left:593px;top:752px">Ornare eu</a>
  <a class="abs" style="left:593px;top:775px">Suspendisse aliquet</a>
  <a class="abs" style="left:593px;top:797px">Enim se</a>
</nav>

<h3 class="abs section-title" style="left:780px">Contact Us</h3>
<div class="abs section-rule" style="left:763px;width:143px"></div>
<div class="abs contact-field" style="top:700px;height:24px">› &nbsp;Name:</div>
<div class="abs contact-field" style="top:731px;height:25px">› &nbsp;Subject</div>
<div class="abs contact-field" style="top:762px;height:56px">› &nbsp;Message</div>
<div class="abs send-button"><svg width="13" height="10" viewBox="0 0 13 10"><path d="M1 5 L5 9 L12 1" fill="none" stroke="#b2233f" stroke-width="2"/></svg></div>

<footer class="abs site-footer">Copyright 2013 © <strong>Lumora Learning</strong>. All Rights Reserved.</footer>
</body>
</html>
```